Illustrate Our Process "Bright Path Method"

We need a graphic design to brand our proprietary process. We are a wealth services team that serves a group of individual and families. Most financial advisors only provide investment management. Our team implements a process that puts our clients goals and finances on a Bright Path foundation.

Please create your own graphic that will simply explain that our elevated process will take care of a client's complete financial picture and in turn put them on a Bright Path foundation.

Our process is called the "Bright Path Method" and it involves:
1) Wealth Management
2) Tax Strategy
3) Cash Management
4) Risk Management
5) Estate Strategy
6) Philanthropy
7) Value Added Services
Note: These things were uploaded in "Bright Path A"

As a person's life becomes more complex they will grow into our process which will constantly ensure their finances & goals are on a Bright Path foundation.

I uploaded pictures of our office so you can see what might go with the overall look and feel of our office if that helps.

Industry/Entity Type

Finance

Requirements
Must have
• The final design should communicate simplicity, stability, expertise and trust. We also want a final design that will quickly describe our process instead of creating confusion.
Nice to have
• We are wanting to put the final design on a canvas print on our bookshelf (which is attached) and have the ability to blow it up and put it on one of our walls.
Should not have
• Clash with the feel and decor of our office

```html
<!DOCTYPE html>
<html lang="en">
<head>
<meta charset="utf-8">
<title>Bright Path Method</title>
<link rel="stylesheet" href="https://fonts.googleapis.com/css2?family=Arimo:wght@700&display=swap">
<style>
  :root {
    --sand: #e4dcbb;
    --ink: #3b3c3e;
    --sun: #f5a31a;
    --glow: #f7b23a;
    --ray: #f3ead0;
    --cliff: #dbb394;
  }
  html, body {
    margin: 0;
    padding: 0;
    width: 1200px;
    height: 600px;
    overflow: hidden;
    background: var(--sand);
  }
  .process-graphic {
    display: block;
    width: 1200px;
    height: 600px;
  }
  .service-label {
    font-family: "Arimo", Arial, sans-serif;
    font-weight: 700;
    font-size: 19px;
    fill: var(--ink);
  }
  .service-icon {
    fill: none;
    stroke: var(--ink);
    stroke-width: 1.6;
    stroke-linecap: round;
    stroke-linejoin: round;
  }
  .method-name {
    font-family: "Arimo", Arial, sans-serif;
    font-weight: 700;
    font-size: 46px;
    fill: var(--ink);
  }
</style>
</head>
<body>
<svg class="process-graphic" viewBox="0 0 1200 600" xmlns="http://www.w3.org/2000/svg" aria-labelledby="graphic-title">
  <title id="graphic-title">Bright Path Method: seven services radiating from a rising sun</title>
  <defs>
    <radialGradient id="sun-glow" cx="598" cy="468" r="420" gradientUnits="userSpaceOnUse">
      <stop offset="0" stop-color="var(--glow)" stop-opacity="1"/>
      <stop offset="0.35" stop-color="var(--glow)" stop-opacity="0.6"/>
      <stop offset="1" stop-color="var(--glow)" stop-opacity="0"/>
    </radialGradient>
  </defs>

  <rect class="backdrop" width="1200" height="600" fill="var(--sand)"/>

  <g class="sunburst">
    <circle cx="598" cy="468" r="420" fill="url(#sun-glow)"/>
    <g fill="none" stroke="#fff" stroke-opacity="0.35" stroke-width="1">
      <circle cx="598" cy="468" r="190"/>
      <circle cx="598" cy="468" r="280"/>
      <circle cx="598" cy="468" r="380"/>
    </g>
    <g stroke="var(--ray)" stroke-width="4" stroke-linecap="round" opacity="0.85">
      <line x1="654" y1="448" x2="1040" y2="307"/>
      <line x1="644" y1="430" x2="958" y2="166"/>
      <line x1="628" y1="416" x2="833" y2="61"/>
      <line x1="608" y1="409" x2="680" y2="3"/>
      <line x1="588" y1="409" x2="516" y2="3"/>
      <line x1="568" y1="416" x2="363" y2="61"/>
      <line x1="552" y1="430" x2="238" y2="166"/>
      <line x1="542" y1="448" x2="156" y2="307"/>
    </g>
  </g>

  <g class="service-labels">
    <text class="service-label" text-anchor="middle" transform="translate(286 294) rotate(30)">Wealth Management</text>
    <text class="service-label" text-anchor="middle" transform="translate(393 227) rotate(50)">Tax Strategy</text>
    <text class="service-label" text-anchor="middle" transform="translate(486 146) rotate(70)">Cash Management</text>
    <text class="service-label" text-anchor="middle" transform="translate(604 144) rotate(-90)">Philanthropy</text>
    <text class="service-label" text-anchor="middle" transform="translate(720 152) rotate(-70)">Estate Strategy</text>
    <text class="service-label" text-anchor="middle" transform="translate(832 200) rotate(-50)">Risk Management</text>
    <text class="service-label" text-anchor="middle" transform="translate(922 289) rotate(-30)">Value Added Services</text>
  </g>

  <g class="service-icons">
    <g class="service-icon" transform="translate(412 358)">
      <path d="M-6 -14 L6 -14 L3 -8 Q14 0 12 10 Q10 16 0 16 Q-10 16 -12 10 Q-14 0 -3 -8 Z"/>
      <text x="0" y="8" text-anchor="middle" font-family="Arimo, sans-serif" font-size="12" fill="var(--ink)" stroke="none">$</text>
    </g>
    <g class="service-icon" transform="translate(460 301)">
      <rect x="-15" y="-10" width="30" height="20" rx="2"/>
      <line x1="-5" y1="6" x2="5" y2="-6"/>
      <circle cx="-6" cy="-4" r="2"/>
      <circle cx="6" cy="4" r="2"/>
    </g>
    <g class="service-icon" transform="translate(524 266)">
      <circle cx="0" cy="0" r="12"/>
      <text x="0" y="5" text-anchor="middle" font-family="Arimo, sans-serif" font-size="13" fill="var(--ink)" stroke="none">$</text>
    </g>
    <g class="service-icon" transform="translate(598 253)">
      <path d="M0 4 L-9 -5 Q-13 -11 -7 -14 Q-3 -15 0 -10 Q3 -15 7 -14 Q13 -11 9 -5 Z"/>
      <path d="M-16 8 L-6 8 Q0 8 4 12 L14 12"/>
    </g>
    <g class="service-icon" transform="translate(672 266)">
      <path d="M-13 0 L0 -12 L13 0"/>
      <path d="M-9 -3 L-9 12 L9 12 L9 -3"/>
      <rect x="-3" y="4" width="6" height="8"/>
    </g>
    <g class="service-icon" transform="translate(736 303)">
      <path d="M-14 0 Q-14 -13 0 -13 Q14 -13 14 0 Q10 -3 7 0 Q3 -3 0 0 Q-3 -3 -7 0 Q-10 -3 -14 0 Z"/>
      <path d="M0 0 L0 12 Q0 16 -4 14"/>
    </g>
    <g class="service-icon" transform="translate(784 360)">
      <path d="M2 -14 L5 -7 L12 -7 L6 -2 L8 5 L2 1 L-4 5 L-2 -2 L-8 -7 L-1 -7 Z"/>
      <path d="M-16 10 L-6 10 Q0 10 4 14 L14 14"/>
    </g>
  </g>

  <rect class="cliff-band" x="0" y="470" width="1200" height="130" fill="var(--cliff)" role="img" aria-label="Desert mesa and sandstone cliff landscape along the horizon"/>

  <circle class="sun-disc" cx="598" cy="468" r="54" fill="var(--sun)"/>

  <text class="method-name" x="600" y="574" text-anchor="middle">Bright Path Method</text>
</svg>
</body>
</html>
```